The Hollow Orchard ebook cover for Corwin Ashby Pellegrew

I need an ebook cover/jpeg that depicts a Middle-Eastern desert and sky. The cover must be very elegant and very austere, the simpler the better.
Toward the top, the text will read: The Hollow Orchard
Directly below the title will read: Bertil Quennoch
The dimensions for the cover should be 2560 pixels (height) and 1600 pixels (width.)

Target Market(s)

Readers of serious magical realism and/or fantasy literature with a serious literary element.

Font styles to use
Serif

Requirements
Must have
• My ebook cover MUST be a painting or illustration depicting a very austere Middle-Eastern desert and desert sky. Must be elegant and austere. The lettering of the title and author name must blend in beautifully with the image--just like fine books in a bookstore. Title must appear at the top: The Hollow Orchard. The author's name must appear below title and read: Bertil Quennoch. Dimensions must be 2560 pixels (height) by 1600 pixels (width)
Nice to have
• A very austere desert on the bottom and a sad elegant sky above.
Should not have
• My ebook cover should not have a spine or a back. I just need an ebook cover of the dimensions stated above.

```html
<!DOCTYPE html>
<html lang="en">
<head>
<meta charset="utf-8">
<title>The Hollow Orchard — Bertil Quennoch</title>
<link rel="stylesheet" href="https://fonts.googleapis.com/css2?family=Cinzel:wght@700;900&family=Cormorant+SC:wght@700&display=swap">
<style>
  :root {
    --sky-top: #4480d2;
    --sky-mid: #2f68bb;
    --sky-bottom: #1b4793;
    --sand-light: #dccaa2;
    --sand-mid: #c7b089;
    --sand-shadow: #a58e68;
    --title-ink: #0f2a57;
    --author-ink: #e2cb9a;
  }
  html, body {
    margin: 0;
    padding: 0;
    overflow: hidden;
    background: #ffffff;
  }
  .cover {
    position: relative;
    width: 750px;
    height: 1200px;
    overflow: hidden;
    background: linear-gradient(180deg, var(--sky-top) 0%, var(--sky-mid) 55%, var(--sky-bottom) 100%);
  }
  .desert {
    position: absolute;
    top: 0;
    left: 0;
    width: 750px;
    height: 560px;
    display: block;
  }
  .title {
    position: absolute;
    top: 622px;
    left: 0;
    width: 750px;
    margin: 0;
    text-align: center;
    font-family: "Cinzel", "Trajan Pro", serif;
    font-weight: 900;
    color: var(--title-ink);
    line-height: 1;
  }
  .title span {
    display: block;
  }
  .title-line-1 { font-size: 86px; }
  .title-line-2 { font-size: 94px; margin-top: -4px; }
  .title-line-3 { font-size: 114px; margin-top: -2px; }
  .author {
    position: absolute;
    top: 950px;
    left: 0;
    width: 750px;
    margin: 0;
    text-align: center;
    font-family: "Cormorant SC", "Cormorant Garamond", serif;
    font-weight: 700;
    font-size: 30px;
    letter-spacing: 0.5px;
    color: var(--author-ink);
  }
</style>
</head>
<body>
  <main class="cover">
    <svg class="desert" viewBox="0 0 750 560" role="img" aria-label="Inverted photograph of pale sandstone desert hills with eroded ridges">
      <defs>
        <linearGradient id="sand-fill" x1="0" y1="0" x2="0" y2="1">
          <stop offset="0" stop-color="var(--sand-light)"/>
          <stop offset="0.55" stop-color="var(--sand-mid)"/>
          <stop offset="1" stop-color="var(--sand-shadow)"/>
        </linearGradient>
      </defs>
      <path fill="url(#sand-fill)" d="M0 0 H750 V500 C735 498 720 496 700 497 C660 499 640 494 610 496 C580 498 560 492 540 494 C510 496 490 504 460 508 C430 512 400 520 370 526 C345 532 320 540 290 544 C265 547 250 538 225 532 C200 527 185 522 160 524 C130 527 105 536 80 542 C60 546 45 532 25 526 C12 522 5 524 0 526 Z"/>
    </svg>

    <h1 class="title">
      <span class="title-line-1">THE</span>
      <span class="title-line-2">HOLLOW</span>
      <span class="title-line-3">ORCHARD</span>
    </h1>

    <p class="author">Bertil Quennoch</p>
  </main>
</body>
</html>
```